Brisk Pelmo Hire - Tara Flyer

Design a catchy flyer to advertise DIY Pelmo Hire (Mini Digger Hire) - Business Name is Brisk Pelmo Hire - Tara. SUMMER SPECIALS ON NOW Points to cover: DIY Hire, 4 in one bucket, trencher, post hole digger, levelling bar, 1/2 day and weekend hire available. Summer specials on now. Now hiring from The Copper Lantern (07) 4928 1176.

```html
<!DOCTYPE html>
<html lang="en">
<head>
<meta charset="utf-8">
<title>Brisk Pelmo Hire – Tara Flyer</title>
<link rel="stylesheet" href="https://fonts.googleapis.com/css2?family=Caprasimo&family=Lato:wght@700;900&family=Oswald:wght@700&display=swap">
<style>
  :root {
    --yellow: #f7d417;
    --red: #d8231f;
    --black: #151515;
    --panel: #222222;
    --white: #ffffff;
    --ink: #111111;
  }
  html, body { margin: 0; padding: 0; overflow: hidden; background: #ffffff; }
  .flyer {
    position: relative;
    width: 937px;
    height: 1200px;
    overflow: hidden;
    background: var(--white);
    font-family: "Lato", sans-serif;
  }
  .hero-photo {
    position: absolute;
    left: 0; top: 18px;
    width: 937px; height: 430px;
    background: linear-gradient(180deg, #c9ccd0 0%, #b8b4aa 35%, #a89a84 60%, #8f8170 100%);
  }
  .shapes { position: absolute; inset: 0; }
  .brand {
    position: absolute;
    left: 34px; top: 58px;
    display: flex; align-items: center; gap: 14px;
    color: var(--ink);
    font-weight: 900;
    font-size: 40px;
    line-height: 1;
    text-transform: uppercase;
  }
  .brand-mark { width: 22px; height: 22px; background: var(--ink); flex: none; }
  .brand-name span { display: block; }
  .specials-bar {
    position: absolute;
    left: 0; top: 548px;
    width: 600px; height: 50px;
    background: linear-gradient(90deg, var(--yellow) 0%, #f3d21a 55%, rgba(247,212,23,0.35) 82%, rgba(247,212,23,0) 100%);
  }
  .specials-title {
    position: absolute;
    left: 28px; top: 550px;
    margin: 0;
    font-family: "Caprasimo", serif;
    font-weight: 400;
    font-size: 34px;
    line-height: 46px;
    color: var(--ink);
  }
  .offer {
    position: absolute;
    left: 29px; top: 618px;
    width: 660px;
    margin: 0;
    color: var(--white);
    font-weight: 700;
    font-size: 30px;
    line-height: 39px;
  }
  .gallery-item {
    position: absolute;
    width: 168px; height: 168px;
    border-radius: 50%;
    border: 5px solid var(--white);
    box-shadow: 0 18px 14px -10px rgba(0,0,0,0.8);
  }
  .gallery-item.post-hole { left: 31px; top: 762px; background: radial-gradient(circle at 50% 40%, #b7a58a, #7c6a52); }
  .gallery-item.excavator { left: 278px; top: 762px; background: linear-gradient(180deg, #8fb0cf 0%, #d6a35a 55%, #7e6c55 100%); }
  .gallery-item.trench { left: 510px; top: 762px; background: linear-gradient(180deg, #cfc7b8 0%, #b59f80 60%, #9b8465 100%); }
  .details {
    position: absolute;
    left: 29px; top: 966px;
    margin: 0;
    color: var(--white);
    font-weight: 700;
    font-size: 18px;
    line-height: 24px;
  }
  .details span { display: block; white-space: nowrap; }
  .machine-photo {
    position: absolute;
    left: 540px; top: 985px;
    width: 380px; height: 215px;
    border-radius: 40px 40px 0 0;
    background: radial-gradient(ellipse at 60% 50%, #c93a2c 0%, #8e1f18 45%, rgba(30,20,20,0) 78%);
  }
  .phone {
    position: absolute;
    left: 862px; top: 686px;
    transform: translate(-50%, -50%) rotate(90deg);
    margin: 0;
    font-family: "Oswald", sans-serif;
    font-weight: 700;
    font-size: 62px;
    line-height: 1;
    letter-spacing: 1px;
    color: var(--white);
    white-space: nowrap;
  }
  .website {
    position: absolute;
    left: 410px; top: 1138px;
    display: flex; align-items: center; gap: 12px;
    font-family: "Oswald", sans-serif;
    font-weight: 700;
    font-size: 30px;
    line-height: 36px;
    color: var(--white);
  }
</style>
</head>
<body>
<main class="flyer">
  <div class="hero-photo" role="img" aria-label="Photo of a yellow excavator with its toothed bucket lowered in a quarry"></div>

  <svg class="shapes" width="937" height="1200" viewBox="0 0 937 1200" aria-hidden="true">
    <defs>
      <linearGradient id="panelShade" x1="0" y1="0" x2="1" y2="1">
        <stop offset="0" stop-color="#2a2a2a"/>
        <stop offset="1" stop-color="#0e0e0e"/>
      </linearGradient>
    </defs>
    <polygon points="0,0 458,0 364,212 0,212" fill="#ffffff"/>
    <polygon points="0,0 440,0 350,198 0,198" fill="var(--yellow)"/>
    <polygon points="700,430 937,430 937,1200 0,1200" fill="var(--red)"/>
    <polygon points="0,423 797,423 722,980 0,1212" fill="url(#panelShade)"
             stroke="#ffffff" stroke-width="22" stroke-linejoin="miter" paint-order="stroke"/>
  </svg>

  <div class="brand">
    <div class="brand-mark"></div>
    <div class="brand-name"><span>Brisk Pelmo</span><span>Hire</span></div>
  </div>

  <div class="specials-bar"></div>
  <h1 class="specials-title">Summer specials on now</h1>

  <p class="offer">DIY Hire, 4 in one bucket, trencher, post hole digger, levelling bar, 1/2 day and weekend hire available.</p>

  <div class="gallery-item post-hole" role="img" aria-label="Photo of a post hole being dug with a hand digger"></div>
  <div class="gallery-item excavator" role="img" aria-label="Photo of an excavator working beside a tree"></div>
  <div class="gallery-item trench" role="img" aria-label="Photo of a digger bucket trenching soil"></div>

  <p class="details">
    <span>Lorem Ipsum is simply dummy text of the printing and</span>
    <span>typesetting industry. Lorem Ipsum has been</span>
    <span>the industry's standard dummy text</span>
    <span>&nbsp;ever since the 1500s,Lorem Ipsum is</span>
    <span>simply dummy text of the printing</span>
    <span>and typesetting industry.</span>
  </p>

  <div class="machine-photo" role="img" aria-label="Photo of a red mini digger loader with a 4 in one bucket attached"></div>

  <p class="phone">(07) 4928 1176</p>

  <div class="website">
    <svg width="26" height="26" viewBox="0 0 26 26" aria-hidden="true" fill="none" stroke="#ffffff" stroke-width="2">
      <circle cx="13" cy="13" r="11"/>
      <ellipse cx="13" cy="13" rx="5" ry="11"/>
      <line x1="2" y1="13" x2="24" y2="13"/>
      <path d="M4 7.5h18M4 18.5h18"/>
    </svg>
    <span>www.briskpelmo.com</span>
  </div>
</main>
</body>
</html>
```